Postcard Design Project A Healthy reminder

Dr.'s Desmond and Lena torvik. Internal Medicine/Family practice. This postcard will be for our patients that we have not seen in a while. Also we need another postcard (the one your designing) with a different heading for New patient's. Do you offer a price break for that? The only thing we would need to change is the heading. Please let me know. Thank you so much! Also can you use the map on the last postcard and our logo I made? I cant find it. Please feel free to call me or email me.

```html
<!DOCTYPE html>
<html lang="en">
<head>
<meta charset="utf-8">
<title>A Healthy Reminder – Postcard</title>
<link rel="stylesheet" href="https://fonts.googleapis.com/css2?family=Barlow+Semi+Condensed:wght@700&family=Lato:wght@400;700&display=swap">
<style>
  :root{
    --brand-red:#7b1a1f;
    --ink:#222222;
    --icon-gray:#8d8f92;
    --band-gray:#939598;
    --rule-gray:#8a8a8a;
    --stage-dark:#3b3b3d;
    --stage-light:#a7a8ab;
    --card-white:#ffffff;
  }
  *{margin:0;padding:0;box-sizing:border-box}
  html,body{width:926px;height:1200px;overflow:hidden}
  body{
    position:relative;
    background:linear-gradient(to bottom,var(--stage-dark) 0,var(--stage-dark) 876px,var(--stage-light) 876px,var(--stage-light) 100%);
    font-family:"Lato",Arial,sans-serif;
    color:var(--ink);
  }
  .postcard{
    position:absolute;left:70px;width:786px;height:524px;
    background:var(--card-white);overflow:hidden;
    box-shadow:2px 3px 6px rgba(0,0,0,.35);
  }
  .postcard--front{top:62px;background:linear-gradient(to right,#e6e6e7 0,#fff 18%,#fff 100%)}
  .postcard--back{top:614px;background:linear-gradient(to right,#fff 0,#fff 75%,#e2e2e3 100%)}
  .arc-art{position:absolute;inset:0;width:786px;height:524px}

  .practice-name{
    position:absolute;font-family:"Lato",Arial,sans-serif;font-weight:700;
    color:var(--ink);white-space:nowrap;
  }
  .practice-tagline{
    position:absolute;font-family:"Lato",Arial,sans-serif;font-weight:700;
    color:var(--ink);letter-spacing:.14em;white-space:nowrap;
  }
  .postcard--front .practice-name{left:34px;top:88px;font-size:15px}
  .postcard--front .practice-tagline{left:66px;top:145px;font-size:8px}

  .stethoscope-art{
    position:absolute;left:226px;top:36px;width:220px;height:104px;border-radius:50px;
    background:radial-gradient(ellipse at center,#d6d6d7 0,#ececed 70%,rgba(255,255,255,0) 100%);
  }

  .headline{
    position:absolute;left:30px;top:172px;
    font-family:"Barlow Semi Condensed","Arial Narrow",sans-serif;font-weight:700;
    color:var(--brand-red);font-size:43px;line-height:1;letter-spacing:-.3px;white-space:nowrap;
  }
  .subhead{
    position:absolute;left:30px;top:218px;
    font-family:"Barlow Semi Condensed","Arial Narrow",sans-serif;font-weight:700;
    color:var(--brand-red);font-size:23px;line-height:1;white-space:nowrap;
  }

  .feature{position:absolute;left:30px;width:440px}
  .feature__icon{position:absolute;left:0;top:0;width:42px;height:42px}
  .feature__title{position:absolute;left:57px;top:0;font-size:14px;font-weight:700;color:var(--brand-red);white-space:nowrap}
  .feature__text{position:absolute;left:57px;top:17px;font-size:13.4px;line-height:17px;color:var(--ink);white-space:nowrap}
  .feature--experienced{top:269px}
  .feature--professional{top:335px}
  .feature--compassionate{top:384px}
  .feature--experienced .feature__icon{top:4px}
  .feature--professional .feature__icon{top:6px}
  .feature--compassionate .feature__icon{top:7px}
  .feature-rule{position:absolute;left:87px;width:224px;height:1.5px;background:var(--rule-gray)}

  .web-band{
    position:absolute;left:0;top:456px;width:460px;height:52px;background:var(--band-gray);
    color:#fff;font-size:19px;font-weight:700;line-height:52px;padding-left:30px;
  }

  .postcard--back .practice-name{left:50px;top:114px;font-size:27px}
  .practice-mark{position:absolute;left:162px;top:60px;width:126px;height:126px;border:2px solid var(--brand-red);transform:rotate(45deg);opacity:0}
  .postcard--back .practice-tagline{left:96px;top:225px;font-size:13px}

  .map-frame{
    position:absolute;left:32px;top:260px;width:314px;height:126px;
    border:3px solid var(--brand-red);border-radius:16px;
    background:linear-gradient(135deg,#eef0ea 0,#e3e6df 45%,#d9dcd6 100%);
  }
  .contact-address{position:absolute;left:32px;top:405px;font-size:13.4px;font-weight:700;color:var(--brand-red);white-space:nowrap}
  .contact-phone{position:absolute;left:32px;top:422px;font-size:32px;font-weight:700;color:var(--brand-red);white-space:nowrap;line-height:1.1}
  .contact-web{position:absolute;left:32px;top:458px;font-size:15px;font-weight:700;color:var(--brand-red);letter-spacing:.28em;white-space:nowrap}

  .stamp-box{position:absolute;left:654px;top:32px;width:99px;height:99px;border:1.5px solid #555}
  .address-line{position:absolute;left:456px;width:297px;height:1.5px;background:#6d6d6d}
</style>
</head>
<body>

<section class="postcard postcard--front" aria-label="Postcard front">
  <svg class="arc-art" viewBox="0 0 786 524" aria-hidden="false">
    <defs>
      <linearGradient id="hallwayTones" x1="0" y1="0" x2="1" y2="1">
        <stop offset="0" stop-color="#c9b39a"/>
        <stop offset="0.5" stop-color="#d9d4cc"/>
        <stop offset="1" stop-color="#9fa7a3"/>
      </linearGradient>
    </defs>
    <path role="img" aria-label="Photo of two doctors in white coats reviewing a patient chart in a clinic hallway"
          d="M452,0 Q592,262 437,524 L786,524 L786,0 Z" fill="url(#hallwayTones)"/>
    <path d="M435,0 Q575,262 420,524" fill="none" stroke="var(--brand-red)" stroke-width="5"/>
    <path d="M446,0 Q586,262 431,524" fill="none" stroke="var(--brand-red)" stroke-width="2.5"/>
  </svg>

  <div class="practice-name">Desmond T Torvik, M.D.</div>
  <div class="practice-tagline">A Primary Care Office</div>
  <div class="stethoscope-art" role="img" aria-label="Faint grey stethoscope illustration"></div>

  <h1 class="headline">A HEALTHY REMINDER.</h1>
  <h2 class="subhead">IT IS TIME FOR YOUR ANNUAL EXAMS</h2>

  <div class="feature feature--experienced">
    <svg class="feature__icon" viewBox="0 0 42 42" aria-hidden="true">
      <g fill="none" stroke="var(--icon-gray)" stroke-width="1.8">
        <ellipse cx="21" cy="21" rx="18" ry="7"/>
        <ellipse cx="21" cy="21" rx="18" ry="7" transform="rotate(60 21 21)"/>
        <ellipse cx="21" cy="21" rx="18" ry="7" transform="rotate(-60 21 21)"/>
      </g>
      <circle cx="21" cy="21" r="2.5" fill="var(--icon-gray)"/>
    </svg>
    <div class="feature__title">Experienced</div>
    <div class="feature__text">Over 20 years of experience practicing in primary<br>care and internal medicine.</div>
  </div>
  <div class="feature-rule" style="top:326px"></div>

  <div class="feature feature--professional">
    <svg class="feature__icon" viewBox="0 0 42 42" aria-hidden="true">
      <circle cx="21" cy="21" r="19" fill="none" stroke="var(--icon-gray)" stroke-width="2"/>
      <path d="M13,21 L19,27 L29,15" fill="none" stroke="var(--icon-gray)" stroke-width="2.2" stroke-linecap="round" stroke-linejoin="round"/>
    </svg>
    <div class="feature__title">Professional</div>
    <div class="feature__text">We maintain exceptional standards of patient care.</div>
  </div>
  <div class="feature-rule" style="top:375px"></div>

  <div class="feature feature--compassionate">
    <svg class="feature__icon" viewBox="0 0 42 42" aria-hidden="true">
      <path d="M21,38 C8,28 2,21 2,13 C2,7 7,3 12,3 C16,3 19,5 21,9 C23,5 26,3 30,3 C35,3 40,7 40,13 C40,21 34,28 21,38 Z"
            fill="none" stroke="var(--icon-gray)" stroke-width="2"/>
    </svg>
    <div class="feature__title">Compassionate</div>
    <div class="feature__text">Commited to providing quality healthcare to<br>our patients we are privileged to serve.</div>
  </div>

  <div class="web-band">www.desmondtorvikmd.com</div>
</section>

<section class="postcard postcard--back" aria-label="Postcard back">
  <svg class="arc-art" viewBox="0 0 786 524" aria-hidden="true">
    <path d="M412,0 Q290,262 440,524" fill="none" stroke="var(--brand-red)" stroke-width="5"/>
    <path d="M424,0 Q302,262 452,524" fill="none" stroke="var(--brand-red)" stroke-width="2.5"/>
  </svg>

  <div class="practice-name">Desmond T Torvik, M.D.</div>
  <div class="practice-tagline">A Primary Care Office</div>

  <div class="map-frame" role="img" aria-label="Street map of north Fresno with a pin marking the office location"></div>

  <div class="contact-address">4820 N. Alder Street Suite 210, Fresno, Ca 93720</div>
  <div class="contact-phone">Office (559) 555-0142</div>
  <div class="contact-web">www.desmondtorvikmd.com</div>

  <div class="stamp-box"></div>
  <div class="address-line" style="top:349px"></div>
  <div class="address-line" style="top:402px"></div>
  <div class="address-line" style="top:456px"></div>
</section>

</body>
</html>
```